Dental Website offering Continuing Educational Courses

Need a Wordpress CMS design for a dentist website which will offer continuing education courses. The design should be professional, simple and elegant. Logo versions are provided. Please follow those colors plus one or two others that will blend well. Here's examples of other sites they like - www.pivotmerrin.com, www.kaltrove.com, www.thebrellinstitute.com., www.qpxa.org/. Please provide designs in jpg format. If selected, then final design will be required in psd format.

Target Market(s)

dentists, endodontists (root canal specialists)

Industry/Entity Type

Education

Requirements
Must have
• Combination Horizontal / Vertical navigation. Place course titles in vertical nav in a side bar on home page. List them as Course 1, Course 2 ,etc.. total of 7 courses. The header horizontal nav should be; Home, About, Courses, Doctor Name, Faculty, FAQ, Patients, Contact.
Need placeholder to accommodate one large static image just under main nav. Need web safe fonts. Need placeholder for calendar like this example www.fennelgates.org/. Need to show a dropdown menu example. Design for 1024 x 768. Need space on home page to allow for logos of external websites/ associations. These are; www.tidemarkguild.com, www.lorvassa.com, www.wlk.org/, www.pomfrettools.com/pomf/. Would like to see a row of images across the bottom of the home page like the www.qpxa.org site has. Would like to show a Contact Form on the home page like the "need assistance" form example on www.thebrellinstitute.com. Would like to create a placeholder on the home page for an image of a doctor.
Nice to have
• 3 or 4 column footer (which features sitemap, copyright, etc..). Examples in the design for the web site’s copy styling:
o through headers
o Bulleted list
o Hyperlink
o Table

```html
<!DOCTYPE html>
<html lang="en">
<head>
<meta charset="utf-8">
<title>Velta Teaching – Continuing Education for Dentists</title>
<link href="https://fonts.googleapis.com/css2?family=Arimo:ital,wght@0,400;0,700;1,400;1,700&family=Questrial&display=swap" rel="stylesheet">
<style>
:root{
  --sky:#16a8ec;
  --sky-light:#35b8f1;
  --navy:#0b4f8e;
  --navy-deep:#0a4580;
  --mid-blue:#1d9fe3;
  --pale-blue:#6cb9e6;
  --side-blue:#1f9fe4;
  --page:#ececec;
  --ink:#222;
  --grey-text:#7a7a7a;
  --link-light:#cde4f6;
  --heading-cyan:#5cc3f6;
  --white:#fff;
}
*{margin:0;padding:0;box-sizing:border-box}
html,body{width:957px;height:1200px;overflow:hidden}
body{position:relative;background:var(--page);font-family:"Arimo",Arial,sans-serif;color:var(--ink)}
.abs{position:absolute}
a{color:inherit;text-decoration:none}
ul{list-style:none}

.topbar{left:0;top:0;width:957px;height:26px;background:linear-gradient(#fafafa,#e2e2e2)}
.call{left:344px;top:2px;font-style:italic;color:#777;font-size:12px}
.call b{font-size:22px;font-weight:400;letter-spacing:.5px;color:#6f6f6f;vertical-align:-3px}
.account{left:761px;top:6px;font-size:12.5px;font-style:italic;color:#1b5fa8;word-spacing:3px}

.sky-band{left:0;top:26px;width:957px;height:350px;background:linear-gradient(var(--sky),var(--sky-light))}
.brand{left:90px;top:50px;width:150px;height:55px;display:flex;align-items:center;gap:8px;font-family:"Questrial",sans-serif;font-size:19px;color:var(--white)}
.brand i{width:12px;height:12px;background:var(--white);display:block}
.search{left:642px;top:78px;width:242px;height:26px;background:var(--white);border-radius:8px}
.search svg{position:absolute;right:10px;top:6px}

.showcase{left:90px;top:125px;width:794px;height:335px;background:#e2e2e2;border-radius:8px;border:1px solid #d4d4d4}
.mainnav{left:92px;top:128px;width:788px;height:38px;background:linear-gradient(#fff,#ececec);border-radius:6px;display:flex;font-size:13.5px;color:#444}
.mainnav li{height:38px;display:flex;align-items:center;justify-content:center;border-right:1px solid #d8d8d8}
.mainnav li:last-child{border-right:0}
.mainnav .current{background:linear-gradient(#2a9ee6,#1a7fcf);color:var(--white);border-radius:6px;margin:3px 5px;height:32px;border:0}
.hero{left:98px;top:174px;width:778px;height:278px;border-radius:6px;background:linear-gradient(90deg,#dfe6ea 0%,#cfdbe2 45%,#e9f0f3 70%,#c9dbe4 100%)}
.dots{left:106px;top:434px;display:flex;gap:8px}
.dots span{width:11px;height:11px;background:#1f90dc;border:1px solid #8ccaf2}
.dropdown{left:97px;top:166px;width:156px;height:181px;background:rgba(34,110,180,.78);border-radius:0 0 8px 8px;padding-top:11px}
.dropdown li{height:27.5px;padding-left:17px;color:var(--white);font-size:11.5px}

.sidebar{left:90px;top:472px;width:204px;height:580px;background:var(--side-blue);border-radius:6px}
.side-title{font-family:"Questrial",sans-serif;font-style:italic;font-size:18px;color:var(--white);padding-left:11px}
.course-list{margin:8px 3px 0}
.course-list li{font-style:italic;font-size:11.5px;color:#b7e2fa;padding:5px 7px 5px;border-bottom:1px solid #3cb0ec;line-height:14px;letter-spacing:.3px}
.course-list li:last-child{border-bottom:0}
.events-head{left:101px;top:877px;width:186px;display:flex;justify-content:space-between;align-items:baseline}
.events-head .side-title{padding:0}
.events-head a{font-size:11.5px;font-weight:700;font-style:italic;color:var(--white)}
.calendar{left:97px;top:900px;width:190px;height:148px;background:#e9f1f8;border:3px solid #9bd1f3;border-radius:7px;padding:3px}
.cal-bar{height:18px;background:linear-gradient(#6d9ccb,#3d73aa);border-radius:4px;color:var(--white);font-size:11px;display:flex;justify-content:space-between;align-items:center;padding:0 4px}
.cal-bar span{width:11px;height:11px;border-radius:50%;background:#8db4d9}
.calendar table{width:100%;border-collapse:separate;border-spacing:2px;font-size:10.5px;text-align:center;margin-top:1px}
.calendar th{font-weight:700;color:#333;height:14px}
.calendar td{background:#d4e6f5;border:1px solid #b8d3ea;height:14px;color:#1b4c80;text-align:right;padding-right:2px}
.calendar td.blank{background:transparent;border:0}
.calendar td.selected{background:#f8e287;border-color:#e3c653;color:#333}
.calendar td.today{color:#e2741c}

.welcome{left:318px;top:487px;font-family:"Questrial",sans-serif;font-style:italic;font-size:19px;color:#222}
.doctor-photo{left:319px;top:518px;width:158px;height:266px;border:4px solid #cfcfcf;background:linear-gradient(#c9ccc9,#3b3d42 55%,#6d6e72)}
.intro{left:488px;top:518px;width:398px;font-style:italic;font-size:11.5px;line-height:13.8px;color:var(--grey-text)}
.intro p{margin-bottom:13.8px}

.feature{top:811px;width:188px;height:101px;border-radius:6px;padding:11px 10px;color:var(--white)}
.feature h3{font-style:italic;font-weight:700;font-size:16.5px;margin-bottom:8px}
.feature p{font-size:11.5px;line-height:13.8px;width:172px}
.feature .go{position:absolute;right:10px;bottom:6px}
.f-pros{left:318px;background:var(--navy)}
.f-root{left:512px;background:var(--mid-blue)}
.f-root p{color:#cfeafb}
.f-help{left:706px;background:var(--pale-blue)}

.footer{left:0;top:928px;width:957px;height:272px;background:linear-gradient(var(--navy),var(--navy-deep))}
.foot-col h4{font-style:italic;font-weight:400;font-size:17px;color:var(--heading-cyan);margin-bottom:5px;letter-spacing:.3px}
.foot-col li{font-style:italic;font-size:12px;color:var(--link-light);height:23px;letter-spacing:.4px}
.partners{left:89px;top:1057px;font-style:italic;font-weight:700;font-size:15.5px;color:#0a3462}
.partner{font-size:13px;color:var(--white);display:flex;align-items:center;gap:6px}
.partner i{width:22px;height:22px;background:var(--white);display:block}
.social{left:760px;top:1110px;display:flex;gap:7px}
.social span{width:26px;height:26px;background:#2c7bc7;border-radius:3px}
.legal{left:527px;top:1168px;display:flex;align-items:center;gap:10px;font-size:12px;font-style:italic;color:var(--link-light);word-spacing:3px}
.legal .mini{font-family:"Questrial",sans-serif;font-style:normal;color:var(--white);font-size:12px;word-spacing:0}
</style>
</head>
<body>
<header>
  <div class="abs topbar"></div>
  <div class="abs call">Call us - <b>061 7320 918</b></div>
  <div class="abs account"><a href="#">Login</a> &nbsp; | &nbsp; <a href="#">Register</a></div>
  <div class="abs sky-band"></div>
  <div class="abs brand"><i></i>Velta Teaching</div>
  <div class="abs search">
    <svg width="13" height="13" viewBox="0 0 13 13"><circle cx="5.5" cy="5.5" r="4" fill="none" stroke="#555" stroke-width="1.8"/><line x1="8.5" y1="8.5" x2="12" y2="12" stroke="#555" stroke-width="2"/></svg>
  </div>
</header>

<div class="abs showcase"></div>
<div class="abs hero" role="img" aria-label="Smiling doctor with stethoscope in a hospital ward"></div>
<div class="abs dots"><span></span><span></span><span></span><span></span><span></span></div>
<ul class="abs mainnav">
  <li class="current" style="width:92px">Home</li>
  <li style="width:88px">About</li>
  <li style="width:97px">Courses</li>
  <li style="width:129px">Doctor Name</li>
  <li style="width:92px">Faculty</li>
  <li style="width:74px">FAQ</li>
  <li style="width:97px">Patients</li>
  <li style="flex:1">Contact</li>
</ul>
<ul class="abs dropdown">
  <li>Submenu Link 1</li><li>Submenu Link 1</li><li>Submenu Link 1</li>
  <li>Submenu Link 1</li><li>Submenu Link 1</li><li>Submenu Link 1</li>
</ul>

<aside class="abs sidebar">
  <h2 class="side-title" style="margin-top:7px">Courses For Doctors</h2>
  <ul class="course-list">
    <li>Functional Occlusion</li>
    <li>Comprehensive Exam &amp; Records<br>Treatment Planning Functional</li>
    <li>Esthetic Excellence</li>
    <li>The Art &amp; Science of Equilibration</li>
    <li>Restoring Anterior Teeth</li>
    <li>Advanced Problem Solving</li>
  </ul>
  <h2 class="side-title" style="margin-top:18px">Courses For Lectures</h2>
  <ul class="course-list">
    <li>Functional Occlusion</li>
    <li>Comprehensive Exam &amp; Records<br>Treatment Planning Functional</li>
    <li>Esthetic Excellence</li>
    <li>The Art &amp; Science of Equilibration</li>
    <li>Restoring Anterior Teeth</li>
    <li>Advanced Problem Solving</li>
  </ul>
</aside>

<main>
  <h1 class="abs welcome">Welcome to Velta Teaching</h1>
  <div class="abs doctor-photo" role="img" aria-label="Dentist in mask and glasses treating a patient"></div>
  <div class="abs intro">
    <p>Lorem ipsum dolor sit amet, consectetuer adipiscing elit, sed diam nonummy nibh euismod tincidunt ut laoreet dolore magna aliquam erat volutpat. Ut wisi enim ad minim veniam, quis nostrud exerci tation ullamcorper suscipit lobortis nisl ut aliquip ex ea commodo consequat.</p>
    <p>Duis autem vel eum iriure dolor in hendrerit in vulputate velit esse molestie consequat, vel illum dolore eu feugiat nulla facilisis at vero eros et accumsan et iusto odio dignissim qui blandit praesent luptatum zzril delenit augue duis dolore te feugait nulla facilisi. Nam liber tempor cum soluta nobis eleifend option congue nihil imperdiet doming id quod mazim placerat facer possim assum.</p>
    <p>Typi non habent claritatem insitam; est usus legentis in iis qui facit eorum claritatem. Investigationes demonstraverunt lectores legere me lius quod ii legunt saepius. Claritas est etiam processus dynamicus, qui sequitur mutationem consuetudium lectorum. Mirum est notare quam littera gothica, quam nunc putamus parum claram, anteposuerit litterarum formas humanitatis per seacula quarta decima et quinta decima. Eodem modo typi, qui nunc nobis videntur parum clari, fiant sollemnes in futurum.</p>
  </div>

  <section class="abs feature f-pros">
    <h3>Meet Professionals</h3>
    <p>With our faculty comprised of over 20 practicing dentists from around the world</p>
    <svg class="go" width="18" height="18" viewBox="0 0 18 18"><circle cx="9" cy="9" r="9" fill="#1c88d6"/><path d="M7.5 5l4 4-4 4" fill="none" stroke="#fff" stroke-width="2"/></svg>
  </section>
  <section class="abs feature f-root">
    <h3>Root Canal Services</h3>
    <p>Stop worrying and discover solutions. Learn the foundation that allows dentists to save time, increase income,</p>
    <svg class="go" width="18" height="18" viewBox="0 0 18 18"><circle cx="9" cy="9" r="9" fill="#0d62ad"/><path d="M7.5 5l4 4-4 4" fill="none" stroke="#fff" stroke-width="2"/></svg>
  </section>
  <section class="abs feature f-help">
    <h3>Need Assistance?</h3>
    <p style="color:#0b3f78">With our faculty comprised of over 20 practicing dentists from around the world</p>
    <svg class="go" width="18" height="18" viewBox="0 0 18 18"><circle cx="9" cy="9" r="9" fill="#1378c8"/><path d="M7.5 5l4 4-4 4" fill="none" stroke="#fff" stroke-width="2"/></svg>
  </section>
</main>

<footer>
  <div class="abs footer"></div>
  <div class="abs foot-col" style="left:346px;top:941px">
    <h4>Areas of Study</h4>
    <ul><li>Core Curriculum</li><li>Advance Restorative</li><li>Dental Medicine</li><li>Practice &amp; Professional Growth</li><li>All Courses »</li></ul>
  </div>
  <div class="abs foot-col" style="left:624px;top:941px">
    <h4>Find a Course</h4>
    <ul><li>For Doctors</li><li>For Lab Techs</li><li>For Hygenients</li><li>Lectures</li><li>Hands-On</li></ul>
  </div>
  <div class="abs foot-col" style="left:826px;top:941px">
    <h4>Products</h4>
    <ul><li>DVDS</li><li>Textooks</li><li>Practice Aids</li><li>All Products »</li></ul>
  </div>

  <h4 class="abs partners">Partners and Associations</h4>
  <div class="abs partner" style="left:88px;top:1097px">Tidemark Guild</div>
  <div class="abs partner" style="left:212px;top:1099px">Lorvassa</div>
  <div class="abs partner" style="left:86px;top:1140px"><i></i>Pomfret Tools</div>
  <div class="abs partner" style="left:232px;top:1140px"><i></i>WLK Academy</div>

  <div class="abs social"><span></span><span></span><span></span><span></span><span></span></div>
  <div class="abs legal"><span class="mini">Velta Teaching</span><span>© All copyrights - 2012 &nbsp;| &nbsp;Privacy Policy &nbsp;| &nbsp;Site map</span></div>
</footer>

<div class="abs events-head"><h2 class="side-title">Events</h2><a href="#">View All Events</a></div>
<div class="abs calendar">
  <div class="cal-bar"><span></span>Jan 2012<span></span></div>
  <table>
    <tr><th>Su</th><th>Mo</th><th>Tu</th><th>We</th><th>Th</th><th>Fr</th><th>Sa</th></tr>
    <tr><td class="blank"></td><td class="blank"></td><td>1</td><td>2</td><td>3</td><td>4</td><td>5</td></tr>
    <tr><td class="selected">6</td><td>7</td><td>8</td><td>9</td><td>10</td><td>11</td><td>12</td></tr>
    <tr><td>13</td><td>14</td><td>15</td><td>16</td><td class="today">17</td><td>18</td><td>19</td></tr>
    <tr><td>20</td><td>21</td><td>22</td><td>23</td><td>24</td><td>25</td><td>26</td></tr>
    <tr><td>27</td><td>28</td><td>29</td><td>30</td><td class="blank"></td><td class="blank"></td><td class="blank"></td></tr>
  </table>
</div>
</body>
</html>
```